Brookmere - a website to encourage people to spend time in nature

I have a squarespace site with some content on it but the squarespace template doesn't completely suit my needs, I keep fiddling with the template but actually I need some professional help to get it looking the way I want and with the right 'mood'.
The website is for "Brookmere" - it will be a blog where I write about the importance of nature for good health. I also want to use the website to market services such as outdoor coaching, retreats and walking workshops.
This has been in my head for a LONG time and I currently only use instagram for micro-blogs but it's time for me to get this moving. I've previously engaged other designers on branding for it but they just didn't get it quite the way that I wanted it and I wasn't completely happy with the results. It's been a process for me as to what I want but in the meantime I just didn't come back to the design aspect of it now. I'm looking for a designer who understands the purpose of the website, the ethos and can help me realise this into a design that's clean, clear and simple.

Please note that I have a domain (brookmere.org) and a lot of content drafted on squarespace already. I have published it with password protection - password is brookmere2020 - it still has some of the original template on it, but does have some content. Don't take it as anything to follow in particular, i am looking for fresh eyes and fresh ideas.

Target Market(s)

There are three main groups that I want to target - people who are suffering from stress and anxiety, people who treat them and parents who want to get their kids outside (thereby preventing stress and anxiety)

Contact Information for Business Card

Helen Corbett
Brookmere
Telephone +44 7942 310587
brookmere@mailpost.net

Logo Text

Brookmere - if that. I have an idea that the logo should have a leaf on it somewhere, or maybe just be a leaf.

Coding

Coded - Design and coding required

Number of Pages Required

5+ page

Font styles to use
Serif
Sans Serif

Colors
add136
33b8a4
34a6d7
3377b5

Requirements
Must have
• Space for lots of images. The ability for me to edit the pages if I need to. Be user friendly. Look beautiful.
• For an idea of the images I use and the content I'm interested in writing about have a look at @brookmere on instagram.
• That pop up about cookies so I am complying with data laws.
Should not have
• Must not be too 'busy' I'd like to avoid too much movement.

```html
<!DOCTYPE html>
<html lang="en">
<head>
<meta charset="utf-8">
<title>Brookmere — My Go-To Forest Walks</title>
<link href="https://fonts.googleapis.com/css2?family=Montserrat:wght@400;500;600;700;800&family=Open+Sans:wght@400;600&display=swap" rel="stylesheet">
<style>
:root{
  --ink:#1b1c1e;
  --text:#555;
  --muted:#aaa;
  --accent:#33b8a4;
  --accent-blue:#3377b5;
  --accent-green:#add136;
  --sky:#34a6d7;
  --line:#e6e6e6;
  --soft:#f1f6f5;
  --dark:#1b1c1e;
  --white:#fff;
}
*{box-sizing:border-box;margin:0;padding:0}
html,body{width:1200px;height:3282px;overflow:hidden;background:var(--white)}
body{position:relative;font-family:"Open Sans",sans-serif;color:var(--text)}
.abs{position:absolute}
.head{font-family:"Montserrat",sans-serif;color:var(--ink)}

/* header */
.site-header{left:0;top:0;width:1200px;height:123px;border:1px solid var(--line)}
.btn-dark{background:var(--dark);color:var(--white);font-family:"Montserrat",sans-serif;font-weight:700;font-size:9px;letter-spacing:.5px;display:flex;align-items:center;justify-content:center;text-transform:uppercase}
.brand{left:0;width:1200px;top:38px;text-align:center;font-family:"Montserrat",sans-serif;font-weight:500;font-size:34px;letter-spacing:2px;color:var(--ink)}
.dot-icon{width:11px;height:11px;border:1.5px solid var(--ink);border-radius:50%}
.menu span{display:block;width:16px;height:2px;background:var(--ink);margin-bottom:4px}

/* section labels */
.label{display:flex;align-items:center;justify-content:center}
.label .box{border:1px solid var(--line);padding:0 16px;height:100%;display:flex;align-items:center;font-family:"Montserrat",sans-serif;font-weight:700;font-size:8.5px;letter-spacing:.8px;color:var(--ink);text-transform:uppercase}
.label .dash{width:8px;height:1px;background:var(--ink);position:absolute;top:50%}

/* sidebar */
.about-text{font-size:8.5px;line-height:16px;text-align:center;color:#555}
.soc{width:20px;height:20px;border-radius:50%;background:var(--ink);display:flex;align-items:center;justify-content:center}
.soc i{width:7px;height:7px;border-radius:50%;background:var(--white);display:block}
.join{border:1px solid var(--ink)}
.join-photo{background:linear-gradient(180deg,#3c4a3e,#263029)}
.join-title{font-family:"Montserrat",sans-serif;font-weight:700;font-size:16px;color:var(--white);text-align:center}
.recent-title{font-family:"Montserrat",sans-serif;font-weight:600;font-size:11px;color:var(--ink)}
.date{font-family:"Montserrat",sans-serif;font-size:8px;letter-spacing:.6px;color:var(--muted)}
.ads{background:var(--soft)}
.cat{font-family:"Montserrat",sans-serif;font-size:10px;color:var(--ink);width:173px;display:flex;justify-content:space-between;border-bottom:1px dashed var(--line);padding-bottom:8px}
.cat span:last-child{color:var(--muted)}

/* article */
.title{font-family:"Montserrat",sans-serif;font-weight:700;font-size:25px;color:var(--ink)}
.meta{font-family:"Montserrat",sans-serif;font-size:8px;letter-spacing:.6px;color:var(--muted);text-transform:uppercase}
.meta b{color:var(--accent);font-weight:600}
.para{width:541px;font-size:8.5px;line-height:16.5px;color:#555}
.quote{width:541px;display:flex;gap:18px}
.quote-mark{font-family:"Montserrat",sans-serif;font-weight:800;font-size:28px;color:var(--accent);line-height:28px;width:26px}
.quote p{border-left:1px solid var(--ink);padding-left:20px;font-family:"Montserrat",sans-serif;font-weight:600;font-size:12px;line-height:20px;color:var(--ink)}
.tags{font-family:"Montserrat",sans-serif;font-size:8.5px;letter-spacing:.5px;color:var(--accent);display:flex;gap:18px}
.divider{height:0;border-top:2px dotted #eaeaea;width:541px}
.avatar{border-radius:50%;background:linear-gradient(160deg,#a9c9bd,#3f6a5e);border:3px solid var(--white);box-shadow:0 0 0 1px var(--line)}
.name{font-family:"Montserrat",sans-serif;font-weight:500;font-size:12.5px;color:var(--ink)}
.small{font-size:8.5px;line-height:16px;color:#555}
.reply{font-family:"Montserrat",sans-serif;font-size:8px;letter-spacing:.6px;color:var(--muted)}
.reply b{color:var(--accent);font-weight:600}
.rel-title{font-family:"Montserrat",sans-serif;font-weight:700;font-size:13.5px;color:var(--ink)}
.field{border:1px solid var(--line);font-size:9px;color:#aaa;padding:15px}

/* subscribe */
.sub-light{background:var(--soft)}
.sub-frame{border:7px solid #e6eceb}
.sub-dark{background:var(--dark)}
.sub-title{font-family:"Montserrat",sans-serif;font-weight:800;font-size:32px;color:var(--ink)}
.send{width:44px;height:44px;border-radius:50%;background:var(--white);display:flex;align-items:center;justify-content:center}

/* footer */
.footer{left:0;top:3010px;width:1200px;height:223px;background:var(--dark)}
.footer p{position:absolute;left:0;width:1200px;text-align:center;color:var(--white);font-size:12.5px}
.copy{left:0;top:3233px;width:1200px;height:49px;background:#28292b;color:var(--white);font-size:10.5px;display:flex;align-items:center;justify-content:center}
</style>
</head>
<body>

<header class="abs site-header">
  <div class="abs btn-dark" style="left:34px;top:61px;width:109px;height:33px">Subscribe</div>
  <div class="abs brand">Brookmere</div>
  <div class="abs dot-icon" style="left:1027px;top:64px"></div>
  <div class="abs dot-icon" style="left:1068px;top:64px"></div>
  <svg class="abs" style="left:1105px;top:64px" width="14" height="11" viewBox="0 0 14 11" aria-label="Email"><rect x=".75" y=".75" width="12.5" height="9.5" fill="none" stroke="#1b1c1e" stroke-width="1.3"/><path d="M1 1l6 5 6-5" fill="none" stroke="#1b1c1e" stroke-width="1.3"/></svg>
  <div class="abs menu" style="left:1153px;top:63px"><span></span><span></span><span></span></div>
</header>

<!-- sidebar -->
<aside>
  <div class="abs label" style="left:219px;top:182px;width:173px;height:30px">
    <span class="dash" style="left:4px"></span><span class="box">About me</span><span class="dash" style="right:4px"></span>
  </div>
  <div class="abs avatar" role="img" aria-label="Portrait photo of the author by a lake" style="left:266px;top:231px;width:80px;height:80px;background:linear-gradient(180deg,#8fae7e,#2f4a44)"></div>
  <p class="abs about-text" style="left:212px;top:332px;width:187px">Helping you slow down, breathe and heal through time spent in nature.</p>
  <div class="abs" style="left:253px;top:379px;display:flex;gap:8px">
    <span class="soc"><i></i></span><span class="soc"><i></i></span><span class="soc"><i></i></span><span class="soc"><i></i></span>
  </div>

  <div class="abs join" style="left:219px;top:438px;width:173px;height:154px">
    <div class="join-photo" role="img" aria-label="Dark photo of tall meadow grass" style="height:100px;display:flex;align-items:center;justify-content:center"><span class="join-title">Join Us Today</span></div>
    <div style="margin:14px 13px 0 18px;border-bottom:1px solid var(--line);padding-bottom:6px;display:flex;justify-content:space-between;font-size:8.5px;color:#aaa">
      <span>Email Address</span>
      <svg width="11" height="8" viewBox="0 0 11 8"><rect x=".5" y=".5" width="10" height="7" fill="none" stroke="#33b8a4"/><path d="M.5.5l5 4 5-4" fill="none" stroke="#33b8a4"/></svg>
    </div>
  </div>

  <div class="abs label" style="left:219px;top:632px;width:173px;height:30px">
    <span class="dash" style="left:0"></span><span class="box">Recent posts</span><span class="dash" style="right:0"></span>
  </div>
  <div class="abs" role="img" aria-label="Sunlit woodland path" style="left:219px;top:682px;width:65px;height:51px;background:linear-gradient(135deg,#e3ecd2,#8fb36a)"></div>
  <div class="abs recent-title" style="left:295px;top:688px">Morning Walks</div>
  <div class="abs date" style="left:295px;top:705px">NOV 23.18</div>
  <div class="abs" role="img" aria-label="Cabin beside a lake" style="left:219px;top:746px;width:65px;height:51px;background:linear-gradient(135deg,#dcebf2,#3f86b0)"></div>
  <div class="abs recent-title" style="left:295px;top:753px">Retreat Notes</div>
  <div class="abs date" style="left:295px;top:770px">NOV 23.18</div>
  <div class="abs" role="img" aria-label="Hands holding autumn leaves" style="left:219px;top:811px;width:65px;height:51px;background:linear-gradient(135deg,#e5efe6,#5fa88f)"></div>
  <div class="abs recent-title" style="left:295px;top:817px">Slow Outdoors</div>
  <div class="abs date" style="left:295px;top:834px">NOV 23.18</div>

  <div class="abs ads" style="left:219px;top:901px;width:173px;height:172px">
    <div class="abs" style="left:14px;top:12px;width:147px;height:147px;background:var(--white)">
      <div class="abs head" style="right:16px;top:105px;font-weight:600;font-size:13px">ads</div>
      <div class="abs" style="right:16px;top:123px;font-size:7.5px;color:#bbb">270 x 270</div>
    </div>
  </div>

  <div class="abs label" style="left:219px;top:1112px;width:173px;height:31px">
    <span class="dash" style="left:0"></span><span class="box">Instagram</span><span class="dash" style="right:0"></span>
  </div>
  <div class="abs" role="img" aria-label="Misty lake at dawn" style="left:219px;top:1163px;width:84px;height:82px;background:linear-gradient(180deg,#e2eef2,#5c98b8)"></div>
  <div class="abs" role="img" aria-label="Fern fronds close up" style="left:309px;top:1163px;width:83px;height:82px;background:linear-gradient(180deg,#e9f1dc,#8cb453)"></div>
  <div class="abs" role="img" aria-label="Walker on a hill path" style="left:219px;top:1252px;width:84px;height:82px;background:linear-gradient(180deg,#e6f0ef,#3fa394)"></div>
  <div class="abs" role="img" aria-label="Meadow grasses in soft light" style="left:309px;top:1252px;width:83px;height:82px;background:linear-gradient(135deg,#eef3e4,#b9cf95)"></div>
  <div class="abs" style="left:219px;top:1345px;width:173px;text-align:center;font-family:Montserrat,sans-serif;font-size:8px;letter-spacing:.6px;color:var(--accent)">@FERNHOLLOW</div>

  <div class="abs label" style="left:219px;top:1392px;width:173px;height:30px">
    <span class="dash" style="left:0"></span><span class="box">Categories</span><span class="dash" style="right:0"></span>
  </div>
  <div class="abs cat" style="left:219px;top:1440px"><span>Wellbeing</span><span>9</span></div>
  <div class="abs cat" style="left:219px;top:1469px"><span>Coaching</span><span>7</span></div>
  <div class="abs cat" style="left:219px;top:1499px"><span>Retreats</span><span>11</span></div>
  <div class="abs cat" style="left:219px;top:1528px"><span>Workshops</span><span>8</span></div>
  <div class="abs cat" style="left:219px;top:1557px;border-bottom:none"><span>Family</span><span>6</span></div>
</aside>

<!-- article -->
<main>
  <h1 class="abs title" style="left:455px;top:174px">My Go-To Forest Walks</h1>
  <div class="abs meta" style="left:455px;top:213px"><b>Wellbeing</b> &nbsp;X&nbsp; Nov 20.18</div>

  <div class="abs" role="img" aria-label="Woman resting on a bench at the edge of a wood" style="left:455px;top:242px;width:541px;height:305px;background:linear-gradient(135deg,#eef4ee,#b7d1bd)"></div>
  <div class="abs" role="img" aria-label="Quiet riverside footpath" style="left:455px;top:553px;width:321px;height:304px;background:linear-gradient(180deg,#e9f2f6,#8fbcd3)"></div>
  <div class="abs" role="img" aria-label="Moss and leaves on a forest floor" style="left:782px;top:553px;width:214px;height:304px;background:linear-gradient(160deg,#eef4e3,#a6c479)"></div>

  <p class="abs para" style="left:455px;top:880px">Time outdoors is one of the simplest ways to calm a busy mind. A short walk under trees lowers stress, steadies the breath and gives the eyes a softer place to rest. In this post I share the routes I return to every week, from the quiet riverside path near my home to the beech wood where I take my coaching clients on slow walks.</p>
  <p class="abs para" style="left:455px;top:947px">None of these walks are long or difficult. What matters is how you move through them: leave the phone in a pocket, notice the sound underfoot, pause when something catches your eye. Many of the people I work with carry anxiety in their shoulders and jaw, and I often see it soften within twenty minutes of walking. Parents tell me the same about their children, who settle, play and talk more freely once they are outside and away from screens.</p>

  <div class="abs quote" style="left:455px;top:1040px">
    <div class="quote-mark">“</div>
    <p>Nature does not hurry, yet everything is accomplished. A slow hour among trees gives back what a busy week takes away.</p>
  </div>

  <p class="abs para" style="left:455px;top:1106px">My first favourite is the riverside loop. It is flat, shaded and easy with a pushchair, and the water keeps a steady rhythm that helps thoughts slow down. I like to stop at the old footbridge and spend a few minutes simply watching the current. If you join one of the walking workshops, this is where we begin, with a short breathing exercise before we set off together along the bank towards the meadow.</p>
  <p class="abs para" style="left:455px;top:1190px">The second is the beech wood on the hill. In spring the floor is covered in bluebells and in autumn the light turns a warm copper. It is a little steeper, so take it gently, rest on the fallen trunks and let the children climb, collect leaves and build small dens among the roots.</p>
  <p class="abs para" style="left:455px;top:1257px">Finally, the open common at dusk. Watching the sky change colour is a lovely way to close the day, and it is the setting for our seasonal evening retreats.</p>

  <div class="abs tags" style="left:455px;top:1306px"><span>#NATURE</span><span>#WELLBEING</span><span>#WALKING</span><span>#FAMILY</span></div>

  <div class="abs btn-dark" style="left:456px;top:1340px;width:117px;height:33px;font-weight:600;letter-spacing:1px">Write comment</div>
  <div class="abs" style="left:583px;top:1340px;width:34px;height:33px;border:1px solid var(--line);display:flex;align-items:center;justify-content:center">
    <svg width="12" height="12" viewBox="0 0 12 12" aria-label="Share"><circle cx="6" cy="2.5" r="1.8" fill="none" stroke="#1b1c1e"/><circle cx="2.5" cy="9" r="1.8" fill="none" stroke="#1b1c1e"/><circle cx="9.5" cy="9" r="1.8" fill="none" stroke="#1b1c1e"/><path d="M5 4l-1.6 3.3M7 4l1.6 3.3M4.3 9h3.4" stroke="#1b1c1e" fill="none"/></svg>
  </div>
  <div class="abs" style="left:839px;top:1355px;font-family:Montserrat,sans-serif;font-size:8.5px;letter-spacing:.6px;color:var(--ink)">2 COMMENTS</div>
  <div class="abs" style="left:918px;top:1355px;font-family:Montserrat,sans-serif;font-size:8.5px;letter-spacing:.6px;color:var(--muted)">9 MINUTES READ</div>

  <div class="abs divider" style="left:455px;top:1406px"></div>

  <div class="abs avatar" role="img" aria-label="Author portrait" style="left:455px;top:1444px;width:64px;height:64px"></div>
  <div class="abs name" style="left:537px;top:1448px">Nadia Pellow</div>
  <p class="abs small" style="left:537px;top:1469px;width:450px">Outdoor coach and nature writer. I lead walking workshops and small retreats for anyone who wants to feel calmer, clearer and more at home outside.</p>
  <div class="abs" style="left:538px;top:1516px;display:flex;gap:12px;align-items:center">
    <i style="width:6px;height:6px;border-radius:50%;background:var(--accent);display:block"></i>
    <i style="width:6px;height:6px;border-radius:50%;background:var(--accent);display:block"></i>
    <i style="width:6px;height:6px;border-radius:50%;background:var(--accent);display:block"></i>
    <svg width="9" height="7" viewBox="0 0 9 7"><rect x=".5" y=".5" width="8" height="6" fill="none" stroke="#33b8a4"/><path d="M.5.5l4 3 4-3" fill="none" stroke="#33b8a4"/></svg>
  </div>

  <div class="abs divider" style="left:455px;top:1557px"></div>

  <div class="abs label" style="left:455px;top:1598px;width:541px;height:31px">
    <span class="dash" style="left:176px"></span><span class="box">Related posts</span><span class="dash" style="right:176px"></span>
  </div>
  <div class="abs" role="img" aria-label="Autumn trees on a hillside" style="left:455px;top:1652px;width:167px;height:140px;background:linear-gradient(180deg,#e4eedd,#93b46c)"></div>
  <div class="abs rel-title" style="left:455px;top:1802px">Autumn Colours</div>
  <div class="abs" role="img" aria-label="Calm river between reeds" style="left:642px;top:1652px;width:167px;height:140px;background:linear-gradient(135deg,#e6f2f6,#5ea9cf)"></div>
  <div class="abs rel-title" style="left:642px;top:1802px">Riverside Calm</div>
  <div class="abs" role="img" aria-label="Coastal path above a beach" style="left:829px;top:1652px;width:167px;height:140px;background:linear-gradient(180deg,#e4f1ef,#4fb3a5)"></div>
  <div class="abs rel-title" style="left:829px;top:1802px">Wild Weekend</div>

  <div class="abs divider" style="left:455px;top:1853px"></div>

  <div class="abs label" style="left:455px;top:1891px;width:541px;height:30px">
    <span class="dash" style="left:186px"></span><span class="box">Comments</span><span class="dash" style="right:186px"></span>
  </div>

  <div class="abs avatar" role="img" aria-label="Commenter portrait" style="left:455px;top:1946px;width:46px;height:46px"></div>
  <div class="abs name" style="left:517px;top:1949px">Nadia Pellow</div>
  <div class="abs reply" style="left:517px;top:1969px">NOV 26.18 &nbsp;X&nbsp; <b>REPLY</b></div>
  <p class="abs small" style="left:517px;top:1987px;width:470px">We tried the riverside loop with the kids on Sunday and it was the calmest afternoon we have had in weeks. Thank you for the gentle ideas.</p>

  <div class="abs divider" style="left:455px;top:2036px"></div>

  <div class="abs avatar" role="img" aria-label="Commenter portrait" style="left:502px;top:2063px;width:46px;height:46px"></div>
  <div class="abs name" style="left:562px;top:2066px">Nadia Pellow</div>
  <div class="abs reply" style="left:562px;top:2086px">NOV 26.18 &nbsp;X&nbsp; <b>REPLY</b></div>
  <p class="abs small" style="left:562px;top:2104px;width:430px">So glad to hear it. Try the beech wood next, the bluebells are worth the climb.</p>

  <div class="abs divider" style="left:455px;top:2163px"></div>

  <div class="abs head" style="left:455px;top:2197px;font-weight:700;font-size:8.5px;letter-spacing:.8px">LEAVE A REPLY</div>
  <div class="abs field" style="left:455px;top:2225px;width:266px;height:34px;padding-top:11px">Your Name</div>
  <div class="abs field" style="left:730px;top:2225px;width:266px;height:34px;padding-top:11px">Your Email</div>
  <div class="abs field" style="left:455px;top:2269px;width:541px;height:89px">Your Comment</div>
  <div class="abs btn-dark" style="left:456px;top:2370px;width:127px;height:31px;font-weight:600;letter-spacing:1px">Post comment</div>
</main>

<div class="abs" style="left:403px;top:2482px;width:621px;height:11px;background:var(--soft)"></div>

<!-- subscribe -->
<section>
  <div class="abs sub-light" style="left:220px;top:2677px;width:352px;height:151px"></div>
  <div class="abs sub-frame" style="left:566px;top:2641px;width:237px;height:220px"></div>
  <div class="abs sub-dark" style="left:595px;top:2677px;width:375px;height:151px"></div>
  <div class="abs sub-title" style="left:283px;top:2734px">Subscribe</div>
  <div class="abs" style="left:666px;top:2745px;width:188px;border-bottom:1px solid #444;padding-bottom:8px;color:var(--white);font-size:9px">Email Address</div>
  <div class="abs send" style="left:862px;top:2735px">
    <svg width="16" height="14" viewBox="0 0 16 14" aria-label="Send"><path d="M1 1l14 6-14 6 3-6z" fill="none" stroke="#1b1c1e" stroke-width="1.3" stroke-linejoin="round"/><path d="M4 7h11" stroke="#1b1c1e" stroke-width="1.3"/></svg>
  </div>
</section>

<footer class="abs footer">
  <p style="top:65px">Helen Corbett</p>
  <p style="top:94px">Brookmere</p>
  <p style="top:124px">Telephone +44 7942 310587</p>
  <p style="top:153px">brookmere@mailpost.net</p>
</footer>
<div class="abs copy">Copyright 2020 Brookmere</div>

</body>
</html>
```